Property investor needs a business card with logo

I need a business card for a UK based business called 'Bright Gate Homes'. I buy houses quickly that is either hard to sell or people have been having trouble to sell. I then create the opportunity for people to buy houses that normally can't. This could be because they have little or no deposit saved up or they don't qualify for a mortgage. The design is to be bright so that it stands out but non threatening and basic. Yellow for the bass colour. The logo to be very simple and represent a house. It could include words like "cant sell? I'll buy it!!" or "Need a quick sale? Let me help" or something as simple as "I buy houses!!" The final design should communicate that I am not some big corporate person that is better that them, but someone that is just a person trying to help them with their situation. with a picture of me with the background removed.
Target Market(s)
Normal everyday people
Industry/Entity Type
Business
Contact Information for Business Card
Gareth Pellingham
07845619027
brightgatehomes@mailbox.example
Font styles to use
Other font styles liked:
- something that looks hand written
Look and feel
Each slider illustrates characteristics of the customer's brand and the style your logo design should communicate.

```html
<!DOCTYPE html>
<html lang="en">
<head>
<meta charset="utf-8">
<title>Bright Gate Homes – Business Card</title>
<link rel="stylesheet" href="https://fonts.googleapis.com/css2?family=Dancing+Script:wght@500&family=Pinyon+Script&family=Open+Sans:wght@400&family=Kalam:wght@400&display=swap">
<style>
  :root {
    --backdrop: #ebe7e1;
    --card-white: #ffffff;
    --brand-yellow: #f7e924;
    --ink: #1b1b1b;
    --ink-soft: #3a3a3a;
    --photo-top: #c9c4bd;
    --photo-bottom: #2c2f36;
  }
  * { margin: 0; padding: 0; box-sizing: border-box; }
  html, body {
    width: 1083px;
    height: 1200px;
    overflow: hidden;
    background: var(--backdrop);
  }
  .card {
    position: absolute;
    border-radius: 34px;
    overflow: hidden;
    box-shadow: 0 4px 14px rgba(0,0,0,0.18);
  }
  .card-front {
    left: 106px;
    top: 74px;
    width: 839px;
    height: 478px;
    background: var(--card-white);
  }
  .card-back {
    left: 112px;
    top: 612px;
    width: 843px;
    height: 482px;
    background: var(--brand-yellow);
    display: flex;
    align-items: center;
    justify-content: center;
  }
  .brand {
    position: absolute;
    left: 50px;
    top: 44px;
    display: flex;
    align-items: center;
    gap: 20px;
  }
  .brand-mark {
    width: 34px;
    height: 34px;
    background: var(--brand-yellow);
  }
  .brand-name {
    font-family: "Dancing Script", cursive;
    font-weight: 500;
    font-size: 44px;
    color: var(--ink);
  }
  .person-name {
    position: absolute;
    left: 44px;
    top: 172px;
    font-family: "Pinyon Script", cursive;
    font-size: 38px;
    color: var(--ink);
  }
  .contact-list {
    position: absolute;
    left: 44px;
    top: 252px;
    list-style: none;
    font-family: "Open Sans", sans-serif;
    font-size: 19px;
    color: var(--ink-soft);
  }
  .contact-list li {
    display: flex;
    align-items: center;
    gap: 12px;
    height: 46px;
  }
  .contact-list svg { width: 16px; height: 16px; fill: var(--ink-soft); }
  .portrait {
    position: absolute;
    left: 520px;
    top: 118px;
    width: 319px;
    height: 360px;
    background: linear-gradient(180deg, var(--photo-top) 0%, var(--photo-bottom) 100%);
  }
  .swoosh {
    position: absolute;
    left: 0;
    top: 0;
    width: 839px;
    height: 478px;
  }
  .tagline {
    position: absolute;
    left: 46px;
    top: 418px;
    font-family: "Kalam", cursive;
    font-size: 30px;
    color: var(--ink);
  }
  .back-name {
    font-family: "Dancing Script", cursive;
    font-weight: 500;
    font-size: 84px;
    color: var(--ink);
  }
</style>
</head>
<body>
  <section class="card card-front">
    <div class="brand">
      <span class="brand-mark"></span>
      <span class="brand-name">Bright Gate Homes</span>
    </div>
    <p class="person-name">Gareth Pellingham</p>
    <ul class="contact-list">
      <li>
        <svg viewBox="0 0 16 16"><path d="M5 1h3v4H6.5c0 2.5 0 4.5 0 6H8v4H5C3.5 13 3 10 3 8s.5-5 2-7z"/></svg>
        <span>07845619027</span>
      </li>
      <li>
        <svg viewBox="0 0 16 16"><path d="M1 6l7-4 7 4v8H1z"/><path d="M2 7l6 4 6-4" fill="none" stroke="#fff" stroke-width="1.2"/></svg>
        <span>brightgatehomes@mailbox.example</span>
      </li>
    </ul>
    <div class="portrait" role="img" aria-label="Cut-out portrait photo of Gareth Pellingham in a dark jacket"></div>
    <svg class="swoosh" viewBox="0 0 839 478" aria-hidden="true">
      <path d="M0 392 C220 360 420 372 620 418 C720 440 790 440 839 424 L839 478 L0 478 Z" fill="var(--brand-yellow)"/>
      <path d="M0 384 C220 350 430 356 620 402 C720 426 790 428 839 414" fill="none" stroke="var(--ink)" stroke-width="3"/>
      <path d="M470 392 C580 402 660 432 839 418 L839 432 C720 446 640 428 470 392 Z" fill="var(--ink)"/>
      <path d="M0 370 C200 344 360 344 470 360 C360 352 200 356 0 378 Z" fill="var(--brand-yellow)"/>
    </svg>
    <p class="tagline">cant sell? I'll buy it!!</p>
  </section>

  <section class="card card-back">
    <span class="back-name">Bright Gate Homes</span>
  </section>
</body>
</html>
```